Information One Page for Email

I am looking for a informative attachment I can send with an introductive email for Ridgeview Cable Works. Something I can also Mail.

Ridgeview Cable Works is the leader in Rebar Post Tension Cable Placement and Post Tension Cable repair. Outside of cable placement and repair we do concrete repair, Parking Garage restoration and

Content

Post Tension Repair and Concrete Restoration
Post-tensioning is a revolutionary method in concrete construction that enhances the strength and durability of structures. However, like all construction ele-ments, post-tension cables can experience wear and damage over time. Ensuring timely and effective repair is crucial for maintaining the safety and integrity of your building.
Why Post-Tension Cable Repair is Essential
1. **Structural Integrity**: Damaged or deteriorated cables can compromise the structural integrity of your building, leading to safety hazards and potential structural failures.
2. **Extended Lifespan**: Regular maintenance and repair of post-tension cables extend the lifespan of your structure, ensuring it remains safe and function-al for years to come.
3. **Cost-Effective**: Addressing cable issues early on prevents more severe damage and costly repairs down the line.
Common Signs of Post-Tension Cable Issues
- Cracks in concrete surfaces
- Unusual noises or popping sounds
- Visible cable ends or broken strands
- Water leakage through cracks
Our Repair Process
1. **Inspection and Assessment**: Our team conducts a thorough inspection to identify the extent of the damage and determine the appropriate repair meth-ods.
2. **Cable Repair or Replacement**: Depending on the severity, we either re-pair the existing cables or replace them with new ones to restore full functional-ity.
3. **Sealing and Protection**: After repairing, we seal the affected areas to protect against moisture and future damage.
4. **Quality Assurance**: We perform rigorous quality checks to ensure the repairs meet industry standards and the structure is safe for use.
Why Choose Us
- **Expertise and Experience**: With years of experience in post-tension cable repair, our team is skilled in handling even the most complex repairs efficiently and effectively.
- **Advanced Technology**: We use the latest technology and materials to ensure durable and long-lasting repairs.
- **Customer Satisfaction**: Our commitment to quality and customer satisfaction sets us apart. We work closely with our clients to ensure their needs are met and expectations exceeded.
Contact Us
If you suspect issues with your post-tension cables or need a routine inspection, don't hesitate to contact us. Our experts are ready to provide the best solutions to keep your structures safe and secure.
Ensure the safety and longevity of your building with our professional post-tension cable repair services. Trust us to deliver quality and reliability every time.

```html
<!DOCTYPE html>
<html lang="en">
<head>
<meta charset="utf-8">
<title>Post Tension Repair and Concrete Restoration – Ridgeview Cable Works</title>
<link href="https://fonts.googleapis.com/css2?family=Baloo+2:wght@400;500;600;700&display=swap" rel="stylesheet">
<style>
  :root {
    --green: #0b6035;
    --green-band: #0a6a3a;
    --ink: #1d1d1d;
    --backdrop: #8a8a8a;
    --paper: #ffffff;
    --muted: #c9c9cf;
    --font: "Baloo 2", sans-serif;
  }
  * { margin: 0; padding: 0; box-sizing: border-box; }
  html, body { width: 1200px; height: 1200px; overflow: hidden; }
  body { background: var(--backdrop); font-family: var(--font); color: var(--ink); }

  .sheet {
    position: absolute; left: 278px; top: 0;
    width: 644px; height: 1200px;
    background: var(--paper); overflow: hidden;
  }
  .brand {
    position: absolute; left: 410px; top: 58px;
    display: flex; align-items: center; gap: 10px;
    color: var(--green); font-weight: 600; font-size: 22px; line-height: 1.05;
    width: 210px;
  }
  .brand-mark { width: 22px; height: 22px; border: 2px solid var(--green); flex: none; }
  .title {
    position: absolute; left: 42px; top: 134px;
    color: var(--green); font-weight: 700; font-size: 32px; line-height: 1.12;
  }
  .intro, .section, .contact { position: absolute; left: 42px; width: 560px; }
  p, li { font-size: 12.5px; line-height: 15px; }
  .intro { top: 284px; text-align: justify; }
  h2 { font-size: 18px; font-weight: 600; line-height: 1.1; margin-bottom: 14px; }
  ol { list-style: none; counter-reset: step; }
  ol li { counter-increment: step; position: relative; padding-left: 68px; }
  ol li::before { content: counter(step) "."; position: absolute; left: 36px; }
  .why { top: 364px; }
  .why ol li { text-align: justify; }
  .signs { top: 546px; }
  .signs ul { list-style: none; margin-left: 0; }
  .process { top: 670px; }
  .choose-band {
    position: absolute; left: 32px; top: 840px; width: 620px; height: 168px;
    background: var(--green-band); color: #fff; padding: 6px 0 0 11px;
  }
  .choose-band h2 { color: #fff; margin-bottom: 14px; }
  .choose-band p { padding-left: 50px; width: 555px; }
  .contact { top: 1018px; }
  .contact p { margin-bottom: 15px; }
  .decor-stripes {
    position: absolute; right: -28px; top: 480px; width: 124px; height: 124px;
    border-radius: 50%; background: #e4e4e8;
  }
  .decor-wedge { position: absolute; left: 0; top: 1091px; }
  .decor-arc { position: absolute; left: 40px; top: 1148px; }
  .decor-corner {
    position: absolute; right: 0; bottom: 0; width: 380px; height: 200px;
    background: radial-gradient(ellipse at 100% 100%, var(--green) 0%, rgba(11,96,53,0.35) 35%, rgba(11,96,53,0) 72%);
  }
</style>
</head>
<body>
<main class="sheet">
  <div class="decor-corner"></div>
  <div class="decor-stripes" role="img" aria-label="Faint striped circle decoration"></div>
  <svg class="decor-wedge" width="36" height="36" viewBox="0 0 36 36"><path d="M0 0 L34 14 L0 34 Z" fill="var(--green)"/></svg>
  <svg class="decor-arc" width="120" height="60" viewBox="0 0 120 60">
    <path d="M12 60 A40 40 0 0 1 52 20 A40 40 0 0 1 60 22" fill="none" stroke="var(--muted)" stroke-width="12"/>
    <circle cx="74" cy="14" r="4" fill="#5aa37a"/>
    <path d="M68 60 A22 22 0 0 1 90 38 L90 60 Z" fill="#cfe3d6"/>
  </svg>

  <div class="brand"><span class="brand-mark"></span><span>Ridgeview Cable Works</span></div>

  <h1 class="title">Post Tension<br>Repair and Concrete<br>Restoration</h1>

  <p class="intro">Post-tensioning is a revolutionary method in concrete construction that enhances the strength and durability of structures. However, like all construction ele-ments, post-tension cables can experience wear and damage over time. Ensuring timely and effective repair is crucial for maintaining the safety and integrity of your building.</p>

  <section class="section why">
    <h2>Why Post-Tension Cable Repair is Essential</h2>
    <ol>
      <li>**Structural Integrity**: Damaged or deteriorated cables can compromise the structural integrity of your building, leading to safety hazards and potential structural failures.</li>
      <li>**Extended Lifespan**: Regular maintenance and repair of post-tension cables extend the lifespan of your structure, ensuring it remains safe and function-al for years to come.</li>
      <li>**Cost-Effective**: Addressing cable issues early on prevents more severe damage and costly repairs down the line.</li>
    </ol>
  </section>

  <section class="section signs">
    <h2>Common Signs of Post-Tension Cable Issues</h2>
    <ul>
      <li>- Cracks in concrete surfaces</li>
      <li>- Unusual noises or popping sounds</li>
      <li>- Visible cable ends or broken strands</li>
      <li>- Water leakage through cracks</li>
    </ul>
  </section>

  <section class="section process">
    <h2>Our Repair Process</h2>
    <ol>
      <li>**Inspection and Assessment**: Our team conducts a thorough inspection to identify the extent of the damage and determine the appropriate repair meth-ods.</li>
      <li>**Cable Repair or Replacement**: Depending on the severity, we either re-pair the existing cables or replace them with new ones to restore full functional-ity.</li>
      <li>**Sealing and Protection**: After repairing, we seal the affected areas to protect against moisture and future damage.</li>
      <li>**Quality Assurance**: We perform rigorous quality checks to ensure the repairs meet industry standards and the structure is safe for use.</li>
    </ol>
  </section>

  <section class="choose-band">
    <h2>Why Choose Us</h2>
    <p>**Expertise and Experience**: With years of experience in post-tension cable repair, our team is skilled in handling even the most complex repairs efficiently and effectively.</p>
    <p>**Advanced Technology**: We use the latest technology and materials to ensure durable and long-lasting repairs.</p>
    <p>**Customer Satisfaction**: Our commitment to quality and customer satisfaction sets us apart. We work closely with our clients to ensure their needs are met and expectations exceeded.</p>
  </section>

  <section class="contact">
    <h2>Contact Us</h2>
    <p>If you suspect issues with your post-tension cables or need a routine inspection, don't hesitate to contact us. Our experts are ready to provide the best solutions to keep your structures safe and secure.</p>
    <p>Ensure the safety and longevity of your building with our professional post-tension cable repair services. Trust us to deliver quality and reliability every time.</p>
    <p>Added Tuesday, 13 January 2026</p>
  </section>
</main>
</body>
</html>
```